Hairdressing Salon called; Velvet Tress. Style Lives Here

Velvet Tress
Style Lives Here
418 Penrose Lane Birch Vale
5183742
Business card not to fussy.
I would like it to be a Black background with White and/or Grey lettering.

I really like the business card attached, so if the front looked like this I would be really happy, but would also like my address and phone number on the front.

On the back I would like two options of
1: reward card; buy any Haircare product over $20 on any visit and on the tenth product receive a complimentry Treatment and
2: appointment times and date

Industry/Entity Type

Business

Contact Information for Business Card

Velvet Tress
Style Lives Here
5183742
418 Penrose Lane, Birch Vale
This must all be included on the front of the card

Font styles to use
Serif
Decorative
Script

Colors
1b1b1b
757575
ffffff

Requirements
Must have
• My phone number and address
Should not have
• Pictures on the front

```html
<!DOCTYPE html>
<html lang="en">
<head>
<meta charset="utf-8">
<title>Velvet Tress – Business Card</title>
<link rel="stylesheet" href="https://fonts.googleapis.com/css2?family=Cinzel:wght@400;600&family=Cormorant+Garamond:wght@500;600&family=Libre+Baskerville:wght@400;700&display=swap">
<style>
  :root {
    --ink: #1b1b1b;
    --grey: #757575;
    --paper: #ffffff;
    --backdrop: #e9e7e4;
    --soft-grey: #bdbdbd;
  }
  * { box-sizing: border-box; margin: 0; padding: 0; }
  html, body { width: 1200px; height: 918px; overflow: hidden; }
  body {
    background: var(--backdrop);
    position: relative;
    font-family: "Libre Baskerville", Georgia, serif;
  }
  .card {
    position: absolute;
    top: 304px;
    width: 540px;
    height: 310px;
    border-radius: 4px;
    box-shadow: 0 8px 24px rgba(0,0,0,.18);
    overflow: hidden;
  }

  /* ---------- Front ---------- */
  .card-front { left: 40px; background: var(--ink); color: var(--paper); }
  .front-frame {
    position: absolute; inset: 20px;
    border: 2px solid var(--paper);
  }
  .corner-ornament {
    position: absolute; width: 24px; height: 24px;
    background: var(--paper); border-radius: 50% 50% 4px 50%;
  }
  .corner-ornament.tl { top: 10px; left: 10px; transform: rotate(180deg); }
  .corner-ornament.tr { top: 10px; right: 10px; transform: rotate(270deg); }
  .corner-ornament.bl { bottom: 10px; left: 10px; transform: rotate(90deg); }
  .corner-ornament.br { bottom: 10px; right: 10px; }
  .front-rule {
    position: absolute; left: 130px; width: 280px; height: 1px;
    background: var(--paper);
  }
  .front-rule.upper { top: 88px; }
  .front-rule.lower { top: 178px; }
  .flourish {
    position: absolute; left: 50%; transform: translateX(-50%);
    width: 130px; height: 26px; border-radius: 13px;
    background: linear-gradient(90deg, transparent, var(--grey) 25%, var(--paper) 50%, var(--grey) 75%, transparent);
  }
  .flourish.upper { top: 54px; }
  .flourish.lower { top: 186px; }
  .salon-name {
    position: absolute; top: 99px; width: 100%; text-align: center;
    font-family: "Cinzel", "Times New Roman", serif;
    font-size: 34px; letter-spacing: 1.5px; font-weight: 400; line-height: 1.2;
  }
  .salon-tagline {
    position: absolute; top: 146px; width: 100%; text-align: center;
    font-family: "Cormorant Garamond", Georgia, serif;
    font-size: 19px; font-weight: 500; letter-spacing: .5px; line-height: 1.2;
  }
  .front-contact {
    position: absolute; top: 230px; width: 100%; text-align: center;
    font-family: "Cormorant Garamond", Georgia, serif;
    font-size: 15px; font-weight: 500; letter-spacing: .6px; line-height: 1.45;
    color: var(--soft-grey);
  }

  /* ---------- Back ---------- */
  .card-back { right: 40px; background: var(--paper); color: var(--ink); padding: 16px 22px; }
  .stamp-row { display: flex; justify-content: space-between; margin-bottom: 8px; }
  .stamp {
    width: 30px; height: 30px; border: 1.5px solid var(--ink); border-radius: 50%;
    display: flex; align-items: center; justify-content: center;
    font-size: 13px;
  }
  .reward-text { font-size: 10.5px; line-height: 1.35; text-align: center; font-weight: 700; }
  .appointment-title {
    margin: 10px auto 0; width: fit-content;
    font-family: "Cinzel", "Times New Roman", serif; font-size: 20px; font-weight: 600;
    border-bottom: 1.5px solid var(--ink); letter-spacing: 1px;
  }
  .title-flourish {
    display: block; margin: 4px auto 6px; width: 110px; height: 10px; border-radius: 5px;
    background: linear-gradient(90deg, transparent, var(--grey) 30%, var(--ink) 50%, var(--grey) 70%, transparent);
  }
  .slots { display: grid; grid-template-columns: 1fr 1fr; column-gap: 26px; row-gap: 7px; }
  .slot {
    display: flex; align-items: flex-end; gap: 4px; font-size: 10.5px; font-weight: 700;
  }
  .slot::after { content: ""; flex: 1; border-bottom: 1px solid var(--ink); margin-bottom: 2px; }
  .contact-line {
    position: absolute; left: 22px; right: 22px; bottom: 14px;
    display: flex; justify-content: space-between; font-size: 10.5px; font-weight: 700;
  }
</style>
</head>
<body>

<section class="card card-front" aria-label="Card front">
  <div class="front-frame"></div>
  <span class="corner-ornament tl" role="img" aria-label="Corner fan ornament"></span>
  <span class="corner-ornament tr" role="img" aria-label="Corner fan ornament"></span>
  <span class="corner-ornament bl" role="img" aria-label="Corner fan ornament"></span>
  <span class="corner-ornament br" role="img" aria-label="Corner fan ornament"></span>
  <div class="flourish upper" role="img" aria-label="Scrolling flourish ornament"></div>
  <div class="front-rule upper"></div>
  <h1 class="salon-name">VELVET TRESS</h1>
  <p class="salon-tagline">: Style Lives Here :</p>
  <div class="front-rule lower"></div>
  <div class="flourish lower" role="img" aria-label="Scrolling flourish ornament"></div>
  <p class="front-contact">418 Penrose Lane, Birch Vale<br>Phone: 5183742</p>
</section>

<section class="card card-back" aria-label="Card back">
  <div class="stamp-row">
    <span class="stamp">1</span><span class="stamp">2</span><span class="stamp">3</span>
    <span class="stamp">4</span><span class="stamp">5</span><span class="stamp">6</span>
    <span class="stamp">7</span><span class="stamp">8</span><span class="stamp">9</span>
    <span class="stamp">10</span>
  </div>
  <p class="reward-text">Buy any Haircare product over $20 on any visit, and on the tenth product brought receive a complimentary Treatment and Blowdry valued at $60.</p>
  <h2 class="appointment-title">APPOINTMENT</h2>
  <span class="title-flourish" role="img" aria-label="Small flourish ornament"></span>
  <div class="slots">
    <div class="slot">Date/Time:</div><div class="slot">Date/Time:</div>
    <div class="slot">Date/Time:</div><div class="slot">Date/Time:</div>
    <div class="slot">Date/Time:</div><div class="slot">Date/Time:</div>
    <div class="slot">Date/Time:</div><div class="slot">Date/Time:</div>
  </div>
  <div class="contact-line">
    <span>Address: 418 Penrose Lane Birch Vale</span>
    <span>Phone: 5183742</span>
  </div>
</section>

</body>
</html>
```